A website for a Maltese Law Firm

Our law firm needs a website to further its business. The site should have a simple yet effective design. We would need the following sections: About us, Practice Areas, About Malta, Contact. These should be further split as follows:

About us: Our firm, Our values, What others say, Offices

Practice Areas: Crimimal, Citizenship & Residence, Harbour Passage Scheme, Criminal Defence, Civil Litigation, Arbitration and ADR, Commercial and Corporate, Media Law.

About Malta: just one section.

Contact: Just one section

We would also need a news feed at the front of the site to include latest news regarding our cases.

At the bottom we need a section for our Terms and a Privacy Statement.

Our logo is being attached.

Target Market(s)

All clients looking for legal assistance in Malta

Industry/Entity Type

Legal

Coding

Coded - Design and coding required

Number of Pages Required

1 page

Requirements
Must have
• It must be simple yet striking.

```html
<!DOCTYPE html>
<html lang="en">
<head>
<meta charset="utf-8">
<title>Galea &amp; Zerafa Advocates</title>
<link href="https://fonts.googleapis.com/css2?family=Montserrat:wght@300;400;500&display=swap" rel="stylesheet">
<style>
  :root {
    --hero-dark: #2b251e;
    --hero-mid: #3d3429;
    --hero-warm: #4a3f32;
    --white: #ffffff;
    --rule: rgba(255,255,255,0.28);
    --button: rgba(150,145,138,0.75);
    --page: #ffffff;
    --ink: #3a3a3a;
    --ink-soft: #555555;
    --icon: #333333;
  }
  * { box-sizing: border-box; margin: 0; padding: 0; }
  html, body { width: 1200px; height: 900px; overflow: hidden; }
  body { font-family: "Montserrat", sans-serif; background: var(--page); color: var(--ink); }

  .hero {
    position: relative; width: 1200px; height: 520px; overflow: hidden;
    background: linear-gradient(120deg, var(--hero-dark) 0%, var(--hero-mid) 55%, var(--hero-warm) 100%);
  }
  .hero-backdrop {
    position: absolute; inset: 0;
    background: linear-gradient(100deg, rgba(0,0,0,0) 30%, rgba(90,78,62,0.35) 60%, rgba(0,0,0,0.15) 100%);
  }
  .site-header {
    position: absolute; top: 0; left: 54px; right: 54px; height: 88px;
    display: flex; align-items: center; border-bottom: 1px solid var(--rule);
  }
  .brand { display: flex; flex-direction: column; align-items: center; color: var(--white); }
  .brand-name { font-size: 20px; font-weight: 400; letter-spacing: 0.5px; line-height: 1.1; }
  .brand-sub { font-size: 7px; font-weight: 400; letter-spacing: 3px; margin-top: 2px; }
  .header-divider { width: 1px; height: 24px; background: var(--rule); margin: 0 26px; }
  .header-phone { display: flex; align-items: center; gap: 8px; color: var(--white); font-size: 14px; }
  .main-nav { margin-left: auto; display: flex; gap: 17px; align-items: center; }
  .main-nav a { color: var(--white); text-decoration: none; font-size: 14px; font-weight: 400; }
  .search-icon { margin-left: 30px; }

  .hero-copy { position: absolute; left: 54px; top: 246px; color: var(--white); }
  .hero-title { font-size: 40px; font-weight: 400; letter-spacing: 0.5px; line-height: 1; }
  .hero-subtitle { font-size: 17px; font-weight: 400; margin-top: 10px; }
  .hero-button {
    display: inline-block; margin-top: 24px; width: 192px; height: 52px; line-height: 52px;
    text-align: center; background: var(--button); color: var(--white);
    font-size: 15px; letter-spacing: 0.3px; text-decoration: none;
  }
  .hero-portrait {
    position: absolute; right: 46px; top: 118px; width: 420px; height: 402px;
    background: radial-gradient(ellipse at 55% 30%, #6b5a4a 0%, #3a3430 45%, #262424 75%, rgba(38,36,36,0) 100%);
    border-radius: 200px 200px 0 0;
  }

  .practice-areas { height: 380px; padding-top: 22px; text-align: center; }
  .section-title { font-size: 24px; font-weight: 300; letter-spacing: 1px; color: var(--ink); }
  .section-rule { width: 44px; height: 1px; background: var(--ink); margin: 10px auto 10px; }
  .section-intro { font-size: 12px; line-height: 1.45; color: var(--ink-soft); }
  .practice-grid {
    display: grid; grid-template-columns: repeat(4, 220px); justify-content: center;
    column-gap: 40px; row-gap: 18px; margin-top: 18px;
  }
  .practice-item { display: flex; flex-direction: column; align-items: center; }
  .practice-icon { width: 44px; height: 40px; }
  .practice-name { font-size: 13px; margin-top: 8px; color: var(--ink); }
  .practice-text { font-size: 11px; line-height: 1.45; margin-top: 7px; color: var(--ink-soft); }
</style>
</head>
<body>
  <section class="hero">
    <div class="hero-backdrop" role="img" aria-label="Dimmed photograph of tall office towers seen from below"></div>
    <header class="site-header">
      <div class="brand">
        <span class="brand-name">GALEA &amp; ZERAFA</span>
        <span class="brand-sub">ADVOCATES</span>
      </div>
      <span class="header-divider"></span>
      <div class="header-phone">
        <svg width="14" height="14" viewBox="0 0 24 24" fill="#fff"><path d="M6.6 10.8a15.1 15.1 0 0 0 6.6 6.6l2.2-2.2a1 1 0 0 1 1-.25 11.4 11.4 0 0 0 3.6.57 1 1 0 0 1 1 1V20a1 1 0 0 1-1 1A17 17 0 0 1 3 4a1 1 0 0 1 1-1h3.5a1 1 0 0 1 1 1c0 1.25.2 2.45.57 3.57a1 1 0 0 1-.25 1z"/></svg>
        <span>(356) 2000 0123</span>
      </div>
      <nav class="main-nav">
        <a href="#">HOME</a>
        <a href="#">ABOUT US</a>
        <a href="#">NEWS</a>
        <a href="#">ABOUT MALTA</a>
        <a href="#">CONTACT &nbsp;US</a>
        <svg class="search-icon" width="20" height="20" viewBox="0 0 24 24" fill="none" stroke="#fff" stroke-width="1.6"><circle cx="10" cy="10" r="7"/><line x1="15" y1="15" x2="22" y2="22"/></svg>
      </nav>
    </header>

    <div class="hero-copy">
      <h1 class="hero-title">CORPORATE AND COMMERCIAL</h1>
      <p class="hero-subtitle">Commission proposes Amendments to Shareholders' Rights Directive</p>
      <a class="hero-button" href="#">LEARN MORE</a>
    </div>

    <div class="hero-portrait" role="img" aria-label="Photograph of a smiling lawyer in a dark suit with arms crossed"></div>
  </section>

  <section class="practice-areas">
    <h2 class="section-title">PRACTICE AREAS</h2>
    <div class="section-rule"></div>
    <p class="section-intro">Lorem ipsum dolor sit amet, consectetur adipiscing elit.<br>Integer posuere erat a ante venenatis dapibus posuere velit aliquet.</p>

    <div class="practice-grid">
      <div class="practice-item">
        <svg class="practice-icon" viewBox="0 0 44 40" fill="none" stroke="var(--icon)" stroke-width="1.4"><circle cx="10" cy="30" r="6"/><circle cx="34" cy="30" r="6"/><circle cx="10" cy="30" r="2.5"/><circle cx="34" cy="30" r="2.5"/><path d="M10 24 V14 Q22 2 34 14 V24"/></svg>
        <div class="practice-name">Crimimal</div>
        <p class="practice-text">Lorem ipsum dolor sit amet,<br>consectetur adipiscing elit.<br>Integer posuere erat.</p>
      </div>
      <div class="practice-item">
        <svg class="practice-icon" viewBox="0 0 44 40" fill="none" stroke="var(--icon)" stroke-width="1.4"><rect x="10" y="3" width="22" height="33"/><path d="M32 6 L36 8 V38 L14 38 L10 36"/><circle cx="21" cy="17" r="6"/><line x1="15" y1="17" x2="27" y2="17"/><line x1="21" y1="11" x2="21" y2="23"/><line x1="15" y1="29" x2="27" y2="29"/></svg>
        <div class="practice-name">Citizenship &amp; Residence</div>
        <p class="practice-text">Lorem ipsum dolor sit amet,<br>consectetur adipiscing elit.<br>Integer posuere erat.</p>
      </div>
      <div class="practice-item">
        <svg class="practice-icon" viewBox="0 0 44 40" fill="none" stroke="var(--icon)" stroke-width="1.4"><path d="M4 14 L12 8 L20 12 L28 8 L40 16"/><path d="M12 8 L4 20"/><path d="M40 16 L32 26 L26 30 L14 22"/><path d="M20 12 L14 18 Q18 22 24 16 L32 24"/><path d="M4 20 L12 26"/></svg>
        <div class="practice-name">Harbour Passage Scheme</div>
        <p class="practice-text">Lorem ipsum dolor sit amet,<br>consectetur adipiscing elit.<br>Integer posuere erat.</p>
      </div>
      <div class="practice-item">
        <svg class="practice-icon" viewBox="0 0 44 40" fill="none" stroke="var(--icon)" stroke-width="1.4"><line x1="22" y1="4" x2="22" y2="34"/><line x1="8" y1="10" x2="36" y2="10"/><path d="M8 10 L3 22 H13 Z"/><path d="M36 10 L31 22 H41 Z"/><line x1="14" y1="36" x2="30" y2="36"/></svg>
        <div class="practice-name">Criminal Defence</div>
        <p class="practice-text">Lorem ipsum dolor sit amet,<br>consectetur adipiscing elit.<br>Integer posuere erat.</p>
      </div>
      <div class="practice-item">
        <svg class="practice-icon" viewBox="0 0 44 40" fill="none" stroke="var(--icon)" stroke-width="1.4"><circle cx="12" cy="8" r="3"/><circle cx="22" cy="8" r="3"/><circle cx="32" cy="8" r="3"/><path d="M7 18 Q12 11 17 18 M17 18 Q22 11 27 18 M27 18 Q32 11 37 18"/><rect x="4" y="18" width="36" height="4"/><rect x="4" y="22" width="36" height="14"/><rect x="8" y="25" width="8" height="8"/><rect x="18" y="25" width="8" height="8"/><rect x="28" y="25" width="8" height="8"/></svg>
        <div class="practice-name">Civil Litigation</div>
        <p class="practice-text">Lorem ipsum dolor sit amet,<br>consectetur adipiscing elit.<br>Integer posuere erat.</p>
      </div>
      <div class="practice-item">
        <svg class="practice-icon" viewBox="0 0 44 40" fill="none" stroke="var(--icon)" stroke-width="1.4"><rect x="14" y="3" width="10" height="14" transform="rotate(-45 19 10)"/><line x1="21" y1="13" x2="8" y2="26"/><rect x="20" y="30" width="16" height="4"/><rect x="16" y="34" width="24" height="4"/></svg>
        <div class="practice-name">Arbitration and ADR</div>
        <p class="practice-text">Lorem ipsum dolor sit amet,<br>consectetur adipiscing elit.<br>Integer posuere erat.</p>
      </div>
      <div class="practice-item">
        <svg class="practice-icon" viewBox="0 0 44 40" fill="none" stroke="var(--icon)" stroke-width="1.4"><rect x="5" y="12" width="34" height="24" rx="2"/><path d="M16 12 V7 H28 V12"/><line x1="5" y1="22" x2="39" y2="22"/><rect x="19" y="19" width="6" height="6"/></svg>
        <div class="practice-name">Commercial and Corporate</div>
        <p class="practice-text">Lorem ipsum dolor sit amet,<br>consectetur adipiscing elit.<br>Integer posuere erat.</p>
      </div>
      <div class="practice-item">
        <svg class="practice-icon" viewBox="0 0 44 40" fill="none" stroke="var(--icon)" stroke-width="1.4"><circle cx="22" cy="20" r="16"/><path d="M28 14 A8 8 0 1 0 28 26"/></svg>
        <div class="practice-name">Media Law</div>
        <p class="practice-text">Lorem ipsum dolor sit amet,<br>consectetur adipiscing elit.<br>Integer posuere erat.</p>
      </div>
    </div>
  </section>
</body>
</html>
```